Webdesign für Vernetzung christlicher Geschäftsleute
Zielgruppe
Die Vereinigung KRTWLE bezweckt die Vernetzung christlicher Geschäftsleute und die Verbreitung von Biblisch fundierten ethischen Geschäftsprinzipien. Die Zielgruppe umfasst Unternehmer und Verantwortungsträger aus Wirtschaft und Politik.
Aufgabenstellung
Ich suche einen Designer, welcher sich ernsthaft mit den Anforderungen und dem Design auseinandersetzt und eine Individuelle Lösung gestaltet.
Das Logo sowie ein unverbindlicher Vorschlag für die Strukturierung liegen bei.
Bitte keine 08/15 Business Stock Fotos (Händeschütteln, Meetings, Präsentationen).
Das Design soll folgende Seiten beinhalten (Beschreibung folgt):
- Startseite
- Standardseite (Titel, Text mit Bildern)
- Event-Detail Seite (Titel, Ort, Datum, ev. Foto, Beschreibungstext, ev. Map)
- Chapter Startseite
Die bestehende Webseite ist kein Massstab ;).

```html
<!DOCTYPE html>
<html lang="de">
<head>
<meta charset="utf-8">
<title>KRTWLE – Startseite</title>
<link rel="stylesheet" href="https://fonts.googleapis.com/css2?family=Open+Sans:wght@400;600;700&family=Cinzel:wght@700&display=swap">
<style>
:root{
  --red:#b0101f;
  --ink:#111;
  --text:#333;
  --band:#ebebeb;
  --paper:#fff;
  --tile:#f2f3f5;
  --numeral:#555;
}
*{margin:0;padding:0;box-sizing:border-box}
html,body{width:740px;height:1200px;overflow:hidden;background:#fafafa}
body{position:relative;font-family:"Open Sans",sans-serif;color:var(--ink)}
.page{position:absolute;left:30px;top:34px;width:680px;height:1132px;background:var(--paper);box-shadow:0 0 24px rgba(0,0,0,.09);overflow:hidden}
.abs{position:absolute}
.band{position:absolute;left:0;width:680px;background:var(--band)}
.band--mid{top:298px;height:315px}
.band--foot{top:997px;height:135px}

.brand{left:80px;top:70px;display:flex;align-items:center;gap:6px;font-weight:700;font-size:15px;color:var(--red);letter-spacing:.5px}
.brand-dot{width:12px;height:12px;border-radius:50%;background:var(--red)}

.nav a{position:absolute;top:72px;font-size:9px;font-weight:700;color:var(--ink);text-decoration:none;letter-spacing:.2px}
.nav .is-active::after{content:"";position:absolute;left:-2px;right:-2px;top:14px;height:1.6px;background:var(--red)}

.hero-photo{left:172px;top:116px;width:400px;height:220px;background:linear-gradient(160deg,#d8d8da 0%,#f3f3f3 30%,#9a9a9a 48%,#e9e9e9 62%,#bdbdbd 75%,#f6f4f4 100%);box-shadow:0 4px 14px rgba(0,0,0,.08)}
.chapter-menu{left:500px;top:127px;display:flex;align-items:center;gap:8px;font-size:8.5px;font-weight:700}
.headline{left:118px;top:160px;display:flex;flex-direction:column;align-items:flex-start}
.headline span{background:var(--paper);font-size:22px;font-weight:700;line-height:30px;padding-right:6px;letter-spacing:.3px}

.section-title{font-size:14.5px;font-weight:700;color:var(--red);letter-spacing:.2px}
.welcome-text{left:92px;top:408px;width:274px;font-size:7.1px;line-height:9.9px;color:var(--text)}

.tile{width:76px;height:49px;background:var(--tile);box-shadow:0 3px 8px rgba(0,0,0,.12);display:flex;align-items:center;justify-content:center;font-family:"Cinzel",serif;font-size:30px;font-weight:700;color:var(--numeral)}
.tile-label{font-size:8.5px;color:var(--ink)}

.events-photo{left:68px;top:552px;width:220px;height:292px;background:linear-gradient(180deg,#eeeeee 0%,#b9b9b9 35%,#8d8d8d 60%,#a7a7a7 100%)}
.events-title{left:90px;top:582px;font-size:22px;font-weight:700}
.events-panel{left:68px;top:844px;width:220px;height:90px;background:var(--band);padding:14px 16px 0 16px;font-size:5.9px;line-height:8.5px;color:var(--text)}
.more{display:flex;align-items:center;justify-content:center;gap:3px;margin-top:9px;font-size:6.2px;font-weight:700;color:var(--ink)}

.event{width:137px}
.event-rule{height:2px;background:var(--ink)}
.event-date{margin-top:12px;font-size:7px;color:var(--red)}
.event-name{margin-top:3px;font-size:6.8px;font-weight:700;letter-spacing:.2px}
.event-venue{margin-top:3px;font-size:7px}
.event-body{margin-top:10px;font-size:5.8px;line-height:8.55px;color:var(--text)}
.event-photo{width:137px;height:90px;background:linear-gradient(180deg,#d7d7d7 0%,#9b9b9b 55%,#6f6f6f 100%)}
.signup{display:flex;align-items:center;gap:5px;font-size:6px;font-weight:700}

.footer-col{font-size:10.6px;line-height:14.6px;color:var(--ink)}
.footer-col strong{display:block;font-size:10px;margin-bottom:4px}
</style>
</head>
<body>
<main class="page">
  <div class="band band--mid"></div>
  <div class="band band--foot"></div>

  <header>
    <div class="abs brand"><span class="brand-dot"></span>KRTWLE</div>
    <nav class="nav">
      <a class="is-active" href="#" style="left:353px">START</a>
      <a href="#" style="left:421px">ÜBER UNS</a>
      <a href="#" style="left:512px">KONTAKT</a>
    </nav>
  </header>

  <section class="hero">
    <div class="abs hero-photo" role="img" aria-label="Schneebedeckter Berggipfel im Nebel"></div>
    <div class="abs chapter-menu">CHAPTER
      <svg width="13" height="11" viewBox="0 0 13 11"><rect y="0" width="13" height="2" fill="#111"/><rect y="4.5" width="13" height="2" fill="#111"/><rect y="9" width="13" height="2" fill="#111"/></svg>
    </div>
    <h1 class="abs headline"><span>SEIN</span><span>ZEICHEN</span><span>ÜBER UNS</span><span>IST LIEBE</span></h1>
  </section>

  <section class="welcome">
    <h2 class="abs section-title" style="left:92px;top:364px">WILLKOMMEN</h2>
    <p class="abs welcome-text">Lorem ipsum dolor sit amet, consetetur sadipscing elitr, sed diam nonumy eirmod tempor invidunt ut labore et dolore magna aliquyam erat, sed diam voluptua. At vero eos et accusam et justo duo dolores et ea rebum. Stet clita kasd gubergren, no sea takimata sanctus est Lorem ipsum dolor sit amet. Lorem ipsum dolor sit amet, consetetur sadipscing elitr, sed diam nonumy eirmod tempor invidunt ute labore et dolore magna aliquyam erat, sed diam voluptua. At vero eos et accusam et justo duo dolores et ea rebum. Stet clita kasd gubergren, no sea takimata sanctus est Lorem ipsum dolor sit amet.</p>
  </section>

  <section class="chapters">
    <h2 class="abs section-title" style="left:422px;top:364px">CHAPTERS</h2>
    <div class="abs tile" style="left:422px;top:403px">I</div>
    <div class="abs tile" style="left:520px;top:403px">II</div>
    <div class="abs tile" style="left:422px;top:486px">III</div>
    <div class="abs tile-label" style="left:422px;top:462px">CHAPTER 1</div>
    <div class="abs tile-label" style="left:522px;top:462px">CHAPTER 2</div>
    <div class="abs tile-label" style="left:424px;top:545px">CHAPTER 3</div>
  </section>

  <section class="events">
    <div class="abs events-photo" role="img" aria-label="Unscharfes Schwarzweissfoto einer Abendveranstaltung mit Gästen an Tischen"></div>
    <h2 class="abs events-title">EVENTS</h2>
    <div class="abs events-panel">
      <p>Lorem ipsum dolor sit amet, consetetur sadipscing elitr, sed diam nonumy eirmod tempor invidunt ut labore et dolore magna aliquyam erat, sed diam voluptua. At vero eos et accusam et justo duo dolores et ea rebum. Stet clita kasd gubergren, no sea takimata sanctus est Lorem ipsum dolor sit amet. Lorem ipsum dolor sit amet, consetetur sadipscing elitr.</p>
      <div class="more">Mehr erfahren
        <svg width="8" height="7" viewBox="0 0 8 7"><path d="M0.5 0.5L3.5 3.5L0.5 6.5M4 0.5L7 3.5L4 6.5" fill="none" stroke="#111" stroke-width="1.4"/></svg>
      </div>
    </div>

    <article class="abs event" style="left:318px;top:643px">
      <div class="event-rule"></div>
      <div class="event-date">22/03/2019</div>
      <div class="event-name">GOTTES IDEE MIT DER AGENTUR M</div>
      <div class="event-venue">LINDENHOF | Hinterbrunn</div>
      <p class="event-body">Lorem ipsum dolor sit amet, consetetur sadipscing elitr, sed diam nonumy eirmod tempor invidunt ut labore et dolore magna aliquyam erat, sed diam voluptua. Ate vero eos et accusam et justo duo dolores et ea rebum. Stet clita kasd gubergren, no sea takimata sanctus est Lorem ipsum dolor sit amet. Lorem ipsum dolor sit amet, consetetur sadipscing elitr, sed diam nonumy eirmod tempor invidunt ute labore et dolore magna aliquyam erat, sed diam voluptua. At vero eos et accusam et justo duo dolores et ea rebum. Stet clita kasd gubergren, no sea takimata sanctus est Lorem ipsum dolor sit amet.</p>
    </article>
    <article class="abs event" style="left:476px;top:643px">
      <div class="event-rule"></div>
      <div class="event-date">23/03/2019</div>
      <div class="event-name">NÄCHSTE GENERALVERSAMMLUNG</div>
      <div class="event-venue">AUBERGE DU CHÊNE | Montvillard</div>
      <p class="event-body">Lorem ipsum dolor sit amet, consetetur sadipscing elitr, sed diam nonumy eirmod tempor invidunt ut labore et dolore magna aliquyam erat, sed diam voluptua. Ate vero eos et accusam et justo duo dolores et ea rebum. Stet clita kasd gubergren, no sea takimata sanctus est Lorem ipsum dolor sit amet. Lorem ipsum dolor sit amet, consetetur sadipscing elitr, sed diam nonumy eirmod tempor invidunt ute labore et dolore magna aliquyam erat, sed diam voluptua. At vero eos et accusam et justo duo dolores et ea rebum. Stet clita kasd gubergren, no sea takimata sanctus est Lorem ipsum dolor sit amet.</p>
    </article>

    <div class="abs event-photo" style="left:318px;top:844px" role="img" aria-label="Schwarzweissfoto des Veranstaltungsgebäudes"></div>
    <div class="abs event-photo" style="left:477px;top:844px" role="img" aria-label="Schwarzweissfoto eines Gasthauses mit Terrasse"></div>

    <div class="abs signup" style="left:364px;top:954px">Anmelden
      <svg width="8" height="7" viewBox="0 0 8 7"><path d="M0.5 0.5L3.5 3.5L0.5 6.5M4 0.5L7 3.5L4 6.5" fill="none" stroke="#b0101f" stroke-width="1.4"/></svg>
    </div>
    <div class="abs signup" style="left:523px;top:951px">Anmelden
      <svg width="8" height="7" viewBox="0 0 8 7"><path d="M0.5 0.5L3.5 3.5L0.5 6.5M4 0.5L7 3.5L4 6.5" fill="none" stroke="#b0101f" stroke-width="1.4"/></svg>
    </div>
  </section>

  <footer>
    <div class="abs footer-col" style="left:95px;top:1040px"><strong>KRTWLE</strong>Kreis der Treuen<br>Wirtschaftsleute Europas</div>
    <div class="abs footer-col" style="left:329px;top:1059px">info@krtwle.de<br>www.krtwle.com</div>
    <div class="abs footer-col" style="left:513px;top:1059px">Datenschutz<br>Impressum</div>
  </footer>
</main>
</body>
</html>
```